Webdesign für Versicherungsmakler
Zielgruppe
Wir sind ein Versicherungsmakler und wollen unseren Internetauftritt modernisieren. Unsere Zielgruppe sind mittelständische Unternehmen. Wir erstellen neben den Sachversicherungen und der Altersvororge auch versicherungsmathematische Gutachten. Wir beraten, erstellen Angebote und verwalten und betreuen die Versicherungsverträge und Schadenfälle unserer Kunden.
Aufgabenstellung
Es besteht bereits eine Website: https://www.k-und-r.example/. An dieser sollte sich orientiert werden, die Inhalte werden vermutlich in Zukunft Ähnlich bleiben.
Der Aufbau der Website soll modernisiert werden. Das Logo soll erhalten bleiben. Die Seite soll einen modernen, cleanen und dennoch zuverlässigen Eindruck vermitteln.

```html
<!DOCTYPE html>
<html lang="de">
<head>
<meta charset="utf-8">
<title>Kranholt &amp; Riemers – Startseite</title>
<link href="https://fonts.googleapis.com/css2?family=Jost:wght@300;400;500;600&display=swap" rel="stylesheet">
<style>
:root{
  --blue:#2e5fa3;
  --blue-dark:#1f3f78;
  --gold:#c9a14a;
  --ink:#1d1f24;
  --muted:#5b5f66;
  --page:#f7f7f8;
  --white:#ffffff;
  --line:#e6e7ea;
}
*{box-sizing:border-box;margin:0;padding:0}
html,body{width:1200px;height:1200px;overflow:hidden}
body{background:var(--page);font-family:"Jost",sans-serif;color:var(--ink);position:relative}

.site-header{position:absolute;left:0;top:0;width:1200px;height:96px;background:var(--white)}
.brand{position:absolute;left:175px;top:30px;display:flex;align-items:center;gap:12px}
.brand-mark{width:36px;height:36px;background:var(--blue)}
.brand-name{font-size:19px;font-weight:400;letter-spacing:1.5px;color:var(--muted);line-height:1.05;text-transform:uppercase}
.meta-nav{position:absolute;right:200px;top:20px;display:flex;gap:22px;font-size:11px;color:var(--muted)}
.main-nav{position:absolute;right:200px;top:56px;display:flex;gap:30px;font-size:13px;font-weight:500}
.main-nav .active{color:var(--blue)}
.meta-nav::after{content:"";position:absolute;left:-20px;right:0;top:24px;border-top:1px solid var(--line)}

.hero{position:absolute;left:0;top:96px;width:1200px;height:486px}
.hero-panel{position:absolute;left:0;top:0;width:580px;height:486px;background:var(--blue);border-bottom-right-radius:14px;z-index:2}
.hero-photo{position:absolute;left:570px;top:0;width:630px;height:486px;background:linear-gradient(120deg,#e9e3d6 0%,#d8d2c4 45%,#6f7378 70%,#eef0f2 100%)}
.hero h1{position:absolute;left:175px;top:126px;width:400px;font-size:27px;font-weight:500;line-height:1.27;color:var(--white)}
.hero p{position:absolute;left:175px;top:258px;width:345px;font-size:11px;line-height:1.8;color:#e6ecf6;font-weight:300}
.btn-gold{position:absolute;left:175px;top:345px;background:var(--gold);color:var(--white);font-size:11.5px;font-weight:500;padding:8px 12px;border-radius:4px}

.teaser-row{position:absolute;left:175px;width:820px;height:245px}
.row-one{top:665px}
.row-two{top:935px}
.photo{position:absolute;top:0;height:245px}
.photo-a{left:0;width:257px;background:linear-gradient(135deg,#3d4a6a,#d7d4cf 60%,#f0ede8)}
.photo-b{left:270px;width:280px;background:linear-gradient(135deg,#9c7a5c,#c8b49c 50%,#8ea0b4)}
.photo-c{left:0;width:257px;background:linear-gradient(135deg,#2f4668,#8797ab 55%,#e3e5e8)}
.photo-d{left:270px;width:280px;background:linear-gradient(135deg,#e4e7eb,#b8c0ca 60%,#5a6b84)}
.card{position:absolute;left:550px;top:0;width:270px;height:245px;background:var(--white);border-radius:0 14px 14px 0;padding:28px 28px}
.eyebrow{font-size:11.5px;color:var(--gold);font-weight:400}
.card h2{font-size:18px;font-weight:500;line-height:1.3;margin-top:14px}
.card p{font-size:11px;line-height:1.6;color:var(--muted);margin-top:12px;font-weight:300}
.link-btn{display:inline-block;margin-top:14px;font-size:11.5px;font-weight:500;color:var(--blue-dark);background:#f1f3f8;padding:8px 11px;border-radius:5px}
</style>
</head>
<body>
<header class="site-header">
  <div class="brand"><span class="brand-mark"></span><span class="brand-name">Kranholt<br>&amp; Riemers</span></div>
  <nav class="meta-nav"><span>Privatkunden</span><span>Für Unternehmen</span><span>Downloads</span><span>Karriere</span></nav>
  <nav class="main-nav"><span class="active">Startseite</span><span>Profil</span><span>Dienstleistungen</span><span>Unternehmen</span><span>Service</span><span>Kontakt</span></nav>
</header>

<section class="hero">
  <div class="hero-panel">
    <h1>Beratung mit Weitblick.<br>Ihre Versicherungslösungen in besten Händen.</h1>
    <p>Herzlich willkommen bei Kranholt &amp; Riemers, Ihren unabhängigen Experten für Versicherungsmanagement und betriebliche Altersversorgung!</p>
    <span class="btn-gold">Beratungstermin vereinbaren!</span>
  </div>
  <div class="hero-photo" role="img" aria-label="Foto eines hellen, modernen Bürogebäudes mit großen Fenstern"></div>
</section>

<section class="teaser-row row-one">
  <div class="photo photo-a" role="img" aria-label="Foto: Beraterin unterschreibt ein Dokument am Schreibtisch"></div>
  <div class="photo photo-b" role="img" aria-label="Foto: älteres Paar schaut gemeinsam auf ein Tablet"></div>
  <article class="card">
    <div class="eyebrow">Altersvorsorge</div>
    <h2>Altersvorsorge, die zu Ihnen passt</h2>
    <p>Wir beraten, optimieren und verwalten – individuell &amp; zuverlässig.</p>
    <span class="link-btn">Mehr erfahren</span>
  </article>
</section>

<section class="teaser-row row-two">
  <div class="photo photo-c" role="img" aria-label="Foto: Besprechung mit Unterlagen am Tisch"></div>
  <div class="photo photo-d" role="img" aria-label="Foto: Hand mit Stift an einem Taschenrechner neben Unterlagen"></div>
  <article class="card">
    <div class="eyebrow">Versicherungsmathematische Gutachten</div>
    <h2>Zukunft planen, Sicherheit gewinnen.</h2>
    <p>Klug vorsorgen, präzise kalkulieren.<br>Wir machen Ihre Zukunft berechenbar!</p>
    <span class="link-btn">Mehr erfahren</span>
  </article>
</section>
</body>
</html>
```